Fashion Design Business Card

I need a new business card designed for a new fashion company. I have attached what I have currently designed. I want it more feminine looking, the logo needs to be gold. I want it simple, feminine and stylish. Please give me some different ideas with the fonts.

I need to send the design we currently have, as we have worked out the logo.
You also need all of our details
Fashion

```html
<!DOCTYPE html>
<html lang="en">
<head>
<meta charset="utf-8">
<title>Marina Fellows – Business Card</title>
<link href="https://fonts.googleapis.com/css2?family=Josefin+Sans:wght@600&family=Tinos:wght@400;700&family=Arimo:wght@400&display=swap" rel="stylesheet">
<style>
  :root {
    --gold: #9a8a4b;
    --pink: #e3178a;
    --ink: #111111;
    --paper: #ffffff;
    --edge: #1a1a1a;
  }
  * { box-sizing: border-box; margin: 0; padding: 0; }
  html, body {
    width: 1200px; height: 412px; overflow: hidden;
    background: var(--paper);
  }
  .sheet { position: relative; width: 1200px; height: 412px; }

  .side-label {
    position: absolute; top: 0;
    font-family: "Arimo", Arial, sans-serif;
    font-size: 21px; line-height: 26px; color: var(--ink);
  }
  .side-label--back { left: 262px; }
  .side-label--front { left: 840px; }

  /* Back of card */
  .card-back {
    position: absolute; left: 16px; top: 36px; width: 578px; height: 370px;
    background: var(--paper);
    border: 1px solid #d9d9d9;
  }
  .brand-block {
    position: absolute; left: 14px; top: 40px; width: 180px; height: 300px;
  }
  .ornament {
    position: absolute; left: 10px; width: 160px; height: 64px;
    border: 3px solid var(--gold);
    border-radius: 32px;
  }
  .ornament::after {
    content: ""; position: absolute; left: 50%; top: 50%;
    width: 12px; height: 12px; margin: -6px 0 0 -6px;
    border-radius: 50%; background: var(--pink);
  }
  .ornament--top { top: 0; }
  .ornament--bottom { bottom: 0; }
  .brand-name {
    position: absolute; left: 0; top: 80px; width: 100%;
    text-align: center;
    font-family: "Josefin Sans", "Century Gothic", sans-serif;
    font-weight: 600; font-size: 22px; line-height: 1.05;
    letter-spacing: 1px; color: var(--ink);
  }
  .brand-role {
    position: absolute; left: 0; top: 138px; width: 100%;
    text-align: center;
    font-family: "Tinos", "Times New Roman", serif;
    font-size: 25px; line-height: 1.05; color: var(--pink);
  }

  .contact {
    position: absolute; left: 218px; top: 152px;
    font-family: "Tinos", "Times New Roman", serif;
    font-size: 19px; line-height: 27px;
  }
  .contact dt { font-weight: 700; color: var(--pink); }
  .contact dd { color: var(--ink); }

  .mark-name {
    position: absolute; left: 350px; top: 50px; width: 200px; height: 150px;
    display: flex; align-items: center; justify-content: center; text-align: center;
    font-family: "Josefin Sans", "Century Gothic", sans-serif;
    font-weight: 600; font-size: 36px; line-height: 1.1; color: var(--gold);
  }

  /* Front of card */
  .card-front {
    position: absolute; left: 580px; top: 26px; width: 620px; height: 386px;
    background: var(--gold);
    padding: 14px;
  }
  .card-front__frame {
    position: relative; width: 100%; height: 100%;
    border: 1.5px solid var(--edge);
  }
  .front-ornament {
    position: absolute; left: 190px; top: 36px; width: 210px; height: 282px;
    border: 4px solid var(--paper);
    border-radius: 60px;
  }
  .front-ornament::before,
  .front-ornament::after {
    content: ""; position: absolute; left: 50%;
    width: 14px; height: 14px; margin-left: -7px;
    border-radius: 50%; background: var(--pink);
  }
  .front-ornament::before { top: 28px; }
  .front-ornament::after { bottom: 28px; }
  .front-name {
    position: absolute; left: 195px; top: 140px; width: 200px;
    text-align: center;
    font-family: "Josefin Sans", "Century Gothic", sans-serif;
    font-weight: 600; font-size: 30px; line-height: 1.15;
    letter-spacing: 1px; color: var(--paper);
  }
  .front-mark {
    position: absolute; top: 154px; width: 100px;
    text-align: center;
    font-family: "Josefin Sans", "Century Gothic", sans-serif;
    font-weight: 600; font-size: 20px; line-height: 1.2; color: var(--pink);
  }
  .front-mark--left { left: 76px; }
  .front-mark--right { left: 414px; }
</style>
</head>
<body>
<main class="sheet">
  <span class="side-label side-label--back">back</span>
  <span class="side-label side-label--front">front</span>

  <section class="card-back" aria-label="Back of business card">
    <div class="brand-block">
      <div class="ornament ornament--top" role="img" aria-label="Gold scroll ornament with pink accent"></div>
      <p class="brand-name">MARINA<br>FELLOWS</p>
      <p class="brand-role">Fashion<br>Designer</p>
      <div class="ornament ornament--bottom" role="img" aria-label="Gold scroll ornament with pink accent"></div>
    </div>

    <dl class="contact">
      <dt>Phone:</dt>
      <dd>0400 312 764</dd>
      <dt>Email:</dt>
      <dd>marina@marinafellows.com</dd>
      <dt>Web:</dt>
      <dd>www.marinafellows.com</dd>
    </dl>

    <p class="mark-name">Marina<br>Fellows</p>
  </section>

  <section class="card-front" aria-label="Front of business card">
    <div class="card-front__frame">
      <div class="front-ornament" role="img" aria-label="White and pink scroll ornament framing the name"></div>
      <p class="front-name">Marina<br>Fellows</p>
      <p class="front-mark front-mark--left">Marina<br>Fellows</p>
      <p class="front-mark front-mark--right">Marina<br>Fellows</p>
    </div>
  </section>
</main>
</body>
</html>
```